Glamour By Tavi

I am a makeup artist looking for professional looking double sided business card. I would like to create a logo and incorporate a set of eyes as the periods above the name "Tavi" on the card.

front of card: Logo "Glamour by Tavi" written across diagonal (bottom left to top right)

Back of card:
1) Professional makeup artist serving New York & New Jersey (or similar to this text)
2) 917-555-0148
3) glamourbytavi@mailcove.com

Industry/Entity Type

Business

```html
<!DOCTYPE html>
<html lang="en">
<head>
<meta charset="utf-8">
<title>Tavi – Business Card</title>
<link rel="stylesheet" href="https://fonts.googleapis.com/css2?family=Arimo:wght@700&display=swap">
<style>
  :root {
    --page-bg: #ffffff;
    --card-dark: #1a1a1a;
    --card-light: #ffffff;
    --ink-dark: #111111;
    --ink-light: #ffffff;
    --artwork-top: #5a5a5a;
    --artwork-bottom: #2c2c2c;
    --card-edge: #cfcfcf;
    --shadow: rgba(0, 0, 0, 0.45);
  }
  html, body {
    margin: 0;
    padding: 0;
    width: 1200px;
    height: 800px;
    overflow: hidden;
    background: var(--page-bg);
  }
  .canvas {
    position: relative;
    width: 1200px;
    height: 800px;
    font-family: "Arimo", Arial, sans-serif;
    font-weight: 700;
  }
  .card {
    position: absolute;
    width: 536px;
    height: 307px;
    box-shadow: 3px 4px 4px var(--shadow);
  }
  .card-front {
    left: 80px;
    top: 127px;
    background: var(--card-dark);
  }
  .eyes-artwork {
    position: absolute;
    left: 147px;
    top: -14px;
    width: 306px;
    height: 120px;
    display: block;
  }
  .front-name {
    position: absolute;
    left: 60px;
    top: 120px;
    margin: 0;
    font-size: 150px;
    line-height: 1;
    letter-spacing: 2px;
    color: var(--ink-light);
  }
  .card-back {
    left: 551px;
    top: 344px;
    background: var(--card-light);
    border: 1px solid var(--card-edge);
    box-sizing: border-box;
    text-align: center;
    color: var(--ink-dark);
  }
  .back-name {
    margin: 78px 0 0;
    font-size: 25px;
    letter-spacing: 1px;
    line-height: 1;
  }
  .back-role {
    margin: 10px 0 0;
    font-size: 17px;
    line-height: 19px;
    letter-spacing: 0.4px;
  }
  .back-phone {
    margin: 18px 0 0;
    font-size: 17px;
    letter-spacing: 0.6px;
  }
  .back-email {
    margin: 9px 0 0;
    font-size: 17px;
    letter-spacing: 0.6px;
  }
</style>
</head>
<body>
  <main class="canvas">
    <section class="card card-front" aria-label="Card front">
      <svg class="eyes-artwork" role="img" aria-label="Illustration of a pair of eyes with long lashes" viewBox="0 0 306 120">
        <defs>
          <linearGradient id="artworkTone" x1="0" y1="0" x2="0" y2="1">
            <stop offset="0" stop-color="var(--artwork-top)"/>
            <stop offset="1" stop-color="var(--artwork-bottom)"/>
          </linearGradient>
        </defs>
        <rect width="306" height="120" rx="8" fill="url(#artworkTone)"/>
      </svg>
      <h1 class="front-name">TAVI</h1>
    </section>

    <section class="card card-back" aria-label="Card back">
      <h2 class="back-name">TAVI</h2>
      <p class="back-role">PROFESSIONAL MAKEUP ARTIST<br>NEW YORK &amp; NEW JERSEY</p>
      <p class="back-phone">917-555-0148</p>
      <p class="back-email">GLAMOURBYTAVI@MAILCOVE.COM</p>
    </section>
  </main>
</body>
</html>
```